Local Motorsports Photography Business Card Design

Looking for a Logo and Business Card design for my father who is a local photographer based in Perth operating under the business name "KLV Photography". Specializing in Motorsports (Torque Racers/Gridcycles/Vorlen Rally) and events photography.
Would like it to look professional, while still maintaining a local/personal feel. Color\Design of the Logo and Card are open to your own interpretation, but should limit the color scheme to around 2-3 colors.
Design should be a logo one side and contact details on the rear. The website currently is very simple and a generic template and should not be used as a basis for design.
Industry/Entity Type
Business
Contact Information for Business Card
Name: Gareth Pindle
Website: www.klvphotography-example.com.au
Email: gareth@klvphotography-example.com.au
Phone: 0455 917 263
Look and feel
Each slider illustrates characteristics of the customer's brand and the style your logo design should communicate.

```html
<!DOCTYPE html>
<html lang="en">
<head>
<meta charset="utf-8">
<title>KLV Photography – Business Card</title>
<link rel="stylesheet" href="https://fonts.googleapis.com/css2?family=Orbitron:wght@700;900&display=swap">
<style>
  :root {
    --page: #ffffff;
    --card-top: #c4c4c4;
    --card-mid: #3a3a3a;
    --card-bottom: #000000;
    --brand-red: #e3141c;
    --text-light: #ffffff;
    --flag-light: #e9e9e9;
    --flag-mid: #7a7a7a;
    --flag-dark: #1a1a1a;
  }
  html, body {
    margin: 0;
    padding: 0;
    width: 1200px;
    height: 900px;
    overflow: hidden;
    background: var(--page);
  }
  .canvas {
    position: relative;
    width: 1200px;
    height: 900px;
  }
  .card {
    position: absolute;
    overflow: hidden;
    background: linear-gradient(to bottom, var(--card-top) 0%, var(--card-mid) 35%, var(--card-bottom) 62%, var(--card-bottom) 100%);
  }
  .card--front { left: 170px; top: 0; width: 804px; height: 446px; }
  .card--back  { left: 166px; top: 453px; width: 803px; height: 447px; }

  .flag-art {
    position: absolute;
    display: block;
    border-radius: 6px;
  }
  .card--front .flag-art { left: 163px; top: 22px; width: 372px; height: 168px; }
  .card--back  .flag-art { left: 164px; top: 64px; width: 363px; height: 200px; }

  .wordmark {
    position: absolute;
    right: 110px;
    top: 196px;
    margin: 0;
    font-family: "Orbitron", sans-serif;
    font-weight: 900;
    color: var(--brand-red);
    text-align: right;
    text-transform: uppercase;
    line-height: 1;
  }
  .wordmark__initials {
    display: block;
    font-size: 110px;
    letter-spacing: 12px;
    margin-right: -12px;
  }
  .wordmark__trade {
    display: block;
    margin-top: 6px;
    font-size: 54px;
    letter-spacing: 4px;
    margin-right: -4px;
  }

  .contact {
    position: absolute;
    left: 0;
    right: 0;
    top: 298px;
    margin: 0;
    padding: 0;
    list-style: none;
    text-align: center;
    font-family: "Orbitron", sans-serif;
    font-weight: 700;
    font-size: 15px;
    letter-spacing: 2px;
    line-height: 35px;
    color: var(--text-light);
    text-transform: uppercase;
  }
</style>
</head>
<body>
<main class="canvas">

  <section class="card card--front" aria-label="Card front">
    <svg class="flag-art" role="img" aria-label="Chequered racing flag on a pole" viewBox="0 0 372 168" preserveAspectRatio="none">
      <defs>
        <linearGradient id="flagTone" x1="0" y1="0" x2="1" y2="1">
          <stop offset="0" stop-color="var(--flag-light)"/>
          <stop offset="0.5" stop-color="var(--flag-mid)"/>
          <stop offset="1" stop-color="var(--flag-dark)"/>
        </linearGradient>
      </defs>
      <rect x="0" y="0" width="372" height="168" fill="url(#flagTone)" opacity="0.85"/>
    </svg>
    <h1 class="wordmark">
      <span class="wordmark__initials">KLV</span>
      <span class="wordmark__trade">Photography</span>
    </h1>
  </section>

  <section class="card card--back" aria-label="Card back">
    <svg class="flag-art" role="img" aria-label="Chequered racing flag on a pole" viewBox="0 0 363 200" preserveAspectRatio="none">
      <defs>
        <linearGradient id="flagToneBack" x1="0" y1="0" x2="1" y2="1">
          <stop offset="0" stop-color="var(--flag-light)"/>
          <stop offset="0.5" stop-color="var(--flag-mid)"/>
          <stop offset="1" stop-color="var(--flag-dark)"/>
        </linearGradient>
      </defs>
      <rect x="0" y="0" width="363" height="200" fill="url(#flagToneBack)" opacity="0.85"/>
    </svg>
    <ul class="contact">
      <li class="contact__web">www.klvphotography-example.com.au</li>
      <li class="contact__email">Email: gareth@klvphotography-example.com.au</li>
      <li class="contact__phone">Phone: 0455 917 263</li>
    </ul>
  </section>

</main>
</body>
</html>
```